VLM8 Print + Graphic Design

We have already used draft hive for our logo design, which has come out really well. Right now we also running a design contest for our business card, please feel free to participate (contest name: VLM8 Business Card Design Project).
We have our logo design completed and we want the creative designers to now come out with all the other designs for VLM8 needs,
1. Brochure design based on the logo colours (4-8 pages)
2. Tri fold flyer designs based on the logo colours
3. Powerpoint templates for our presentations
4. Letter head designs (A4 & A3)
5. Tech Cases (http://www.brantholm.com.au/webapp/wcs/stores/servlet/ProductDisplay?storeId=47819&langId=10&catalogId=31870&categoryId=512947&productId=48203916&imagePath=QTB0042907)
There should be synergy and continuance across all designs, we use a lot of power-point presentations and continued changes to brochures, so we need these to stand out in graphic design with elegance and class.
Powerpoint / Brochure / Flyer should have the following,
1. Place for photos, charts, texts and sections.
2. Final page to contain our contact details (social + mobile + address)
3. Templates editable by word or powerpoint or illustrator
Thank you and all the best.
For details about the company please visit, www.vlm8.com.
visit www.vlm8.com
Graphic Design

```html
<!DOCTYPE html>
<html lang="en">
<head>
<meta charset="utf-8">
<title>VLM8 Powerpoint Presentation – set 01</title>
<link href="https://fonts.googleapis.com/css2?family=Gelasio:ital@0;1&family=Ubuntu:wght@300;400;500&family=Open+Sans:wght@400&display=swap" rel="stylesheet">
<style>
  :root {
    --board: #2a2e2d;
    --board-line: #323736;
    --lime: #b2d445;
    --teal: #5bbf8f;
    --ink: #1b1b1b;
    --body-text: #6d6d6d;
    --sub-brown: #7b6a5c;
    --caption: #b3d155;
    --white: #ffffff;
  }
  * { margin: 0; padding: 0; box-sizing: border-box; }
  html, body { width: 1200px; height: 748px; overflow: hidden; }
  body {
    position: relative;
    background: var(--board);
    background-image:
      repeating-linear-gradient(45deg, var(--board-line) 0 1px, transparent 1px 4px),
      repeating-linear-gradient(-45deg, var(--board-line) 0 1px, transparent 1px 4px);
    font-family: "Ubuntu", sans-serif;
  }
  .board-title {
    position: absolute; top: 28px; left: 0; width: 1200px;
    text-align: center;
    font: 400 25px "Gelasio", serif;
    color: var(--caption);
  }
  .slide-frame { position: absolute; width: 488px; height: 275px; }
  .slide-frame--1 { left: 79px;  top: 92px; }
  .slide-frame--2 { left: 647px; top: 92px; }
  .slide-frame--3 { left: 79px;  top: 418px; }
  .slide-frame--4 { left: 647px; top: 418px; }
  .page-caption {
    position: absolute; right: 0; top: 279px;
    font: italic 400 15px "Gelasio", serif;
    color: var(--caption);
  }
  .slide {
    position: absolute; left: 0; top: 0;
    width: 480px; height: 270px;
    background: var(--white);
    overflow: hidden;
    transform: scale(1.0167);
    transform-origin: 0 0;
  }
  .slide > * { position: absolute; }

  /* cover slide */
  .cover-bar { left: 24px; top: 80px; width: 24px; height: 100px; background: var(--lime); }
  .cover-title {
    left: 62px; top: 101px;
    font: 500 22px "Ubuntu", sans-serif; color: var(--ink);
    white-space: nowrap;
  }
  .cover-title .brand { color: var(--teal); margin-left: 4px; }
  .cover-subtitle {
    left: 62px; top: 131px;
    font: 400 10.5px "Ubuntu", sans-serif; color: var(--sub-brown); letter-spacing: .2px;
  }

  /* inner slide structure */
  .top-tab { left: 0; top: 0; width: 110px; height: 11px; background: var(--lime); }
  .brand-mark {
    left: 10px; top: 21px;
    font: 500 20px "Ubuntu", sans-serif; color: var(--teal);
    display: flex; align-items: center; gap: 4px;
  }
  .brand-mark .dot { width: 9px; height: 9px; border-radius: 50%; background: var(--lime); }
  .section-panel { left: 0; top: 60px; width: 106px; height: 178px; background: var(--lime); }
  .section-label {
    top: 68px;
    font: 300 18px "Ubuntu", sans-serif; color: var(--white);
  }
  .section-label--about { left: 40px; }
  .section-label--services { left: 19px; }
  .photo-area { left: 108px; top: 60px; width: 132px; height: 80px; }
  .photo-area--about { background: linear-gradient(135deg, #5a5e66 0%, #9aa3ad 45%, #dfe4e8 100%); }
  .photo-area--it { left: 106px; width: 134px; background: linear-gradient(135deg, #1e2a38 0%, #3d5870 50%, #7d98ad 100%); }
  .accent-block { left: 108px; top: 140px; width: 132px; height: 98px; background: var(--teal); }
  .accent-block--it { left: 106px; top: 142px; width: 134px; height: 96px; }
  .body-copy {
    left: 250px; top: 58px; width: 220px;
    font: 400 6.2px/1.45 "Open Sans", sans-serif; color: var(--body-text);
  }
  .body-copy p + p { margin-top: 7px; }
  .body-copy--it { top: 56px; }

  /* services list */
  .service-column { left: 108px; top: 60px; width: 132px; height: 178px; background: var(--teal); }
  .service-list { left: 196px; top: 66px; list-style: none; }
  .service-list li { display: flex; align-items: center; height: 34px; white-space: nowrap; }
  .service-list svg { width: 8px; height: 14px; margin-right: 3px; }
  .service-number { font: 400 17px "Ubuntu", sans-serif; color: var(--ink); width: 32px; }
  .service-name { font: 400 11.5px "Ubuntu", sans-serif; color: var(--ink); margin-left: 10px; }
  .service-heading {
    left: 124px; top: 153px;
    font: 400 11.5px/1.2 "Ubuntu", sans-serif; color: var(--white);
  }
  .service-heading span { display: block; padding-left: 15px; }
  .section-icon { left: 88px; top: 154px; width: 12px; height: 12px; }

  /* footer band */
  .footer-band {
    left: 0; top: 252px; width: 480px; height: 18px;
    background: var(--teal);
    display: flex; align-items: center;
    font: 400 5.6px "Open Sans", sans-serif; color: var(--white);
  }
  .footer-address { margin-left: 9px; }
  .footer-dot { width: 6px; height: 6px; border-radius: 50%; background: var(--white); margin: 0 8px 0 8px; }
  .footer-company { font-size: 6.4px; }
  .footer-nav { margin-left: auto; margin-right: 6px; display: flex; align-items: center; gap: 3px; font-size: 6.4px; }
  .footer-nav svg { width: 5px; height: 7px; }
</style>
</head>
<body>
  <h1 class="board-title">Powerpoint Presentation (set 01)</h1>

  <!-- page 1 -->
  <section class="slide-frame slide-frame--1">
    <div class="slide">
      <div class="cover-bar"></div>
      <h2 class="cover-title">INTRODUCTION TO <span class="brand">VLM8</span></h2>
      <p class="cover-subtitle">POWERPOINT PRESENTATION</p>
      <footer class="footer-band">
        <span class="footer-address">118 Larkfield Row 07, 9th Avenue Dunmore, Calvera, 368041</span>
        <span class="footer-dot"></span>
        <span class="footer-company">VLM8 Pty Ltd</span>
        <span class="footer-nav">01
          <svg viewBox="0 0 5 7"><polyline points="1,0.5 4,3.5 1,6.5" fill="none" stroke="#fff" stroke-width="1.4"/></svg>
        </span>
      </footer>
    </div>
    <p class="page-caption">1st page</p>
  </section>

  <!-- page 2 -->
  <section class="slide-frame slide-frame--2">
    <div class="slide">
      <div class="top-tab"></div>
      <div class="brand-mark"><span class="dot"></span>VLM8</div>
      <div class="section-panel"></div>
      <h2 class="section-label section-label--about">ABOUT</h2>
      <div class="photo-area photo-area--about" role="img" aria-label="Photo of a hand holding floating media screens"></div>
      <div class="accent-block"></div>
      <div class="body-copy">
        <p>We all know the saying to seize the opportunity as it comes along because it only comes once.</p>
        <p>We believe in creating opportunities. With our diverse interests in portfolios, the company aims to provide its clients with the flexibility of choice to define their needs for services and acquire only the specific services. We promise to deliver quality services across several industries in setting up franchises or partnering services.</p>
        <p>The company has been formed by a group of people with significant knowledge and experience in Technology but also extending the company's horizon into Extreme Sports, Childcare and Food to name a few.</p>
        <p>We believe in making a difference. We value innovation, value and exceptional service for your investment, and empowering people who work with us.</p>
      </div>
      <footer class="footer-band">
        <span class="footer-address">118 Larkfield Row 07, 9th Avenue Dunmore, Calvera, 368041</span>
        <span class="footer-dot"></span>
        <span class="footer-company">VLM8 Pty Ltd</span>
        <span class="footer-nav">
          <svg viewBox="0 0 5 7"><polyline points="4,0.5 1,3.5 4,6.5" fill="none" stroke="#fff" stroke-width="1.4"/></svg>02
          <svg viewBox="0 0 5 7"><polyline points="1,0.5 4,3.5 1,6.5" fill="none" stroke="#fff" stroke-width="1.4"/></svg>
        </span>
      </footer>
    </div>
    <p class="page-caption">2nd page</p>
  </section>

  <!-- page 3 -->
  <section class="slide-frame slide-frame--3">
    <div class="slide">
      <div class="top-tab"></div>
      <div class="brand-mark"><span class="dot"></span>VLM8</div>
      <div class="section-panel"></div>
      <h2 class="section-label section-label--services">SERVICES</h2>
      <div class="service-column"></div>
      <ul class="service-list">
        <li><svg viewBox="0 0 8 14"><polyline points="1,1 7,7 1,13" fill="none" stroke="#1b1b1b" stroke-width="0.8"/></svg><span class="service-number">01</span><span class="service-name">INFORMATION TECHNOLOGY</span></li>
        <li><svg viewBox="0 0 8 14"><polyline points="1,1 7,7 1,13" fill="none" stroke="#1b1b1b" stroke-width="0.8"/></svg><span class="service-number">02</span><span class="service-name">FOOD SERVICES</span></li>
        <li><svg viewBox="0 0 8 14"><polyline points="1,1 7,7 1,13" fill="none" stroke="#1b1b1b" stroke-width="0.8"/></svg><span class="service-number">03</span><span class="service-name">CHILD CARE&nbsp; CENTRES</span></li>
        <li><svg viewBox="0 0 8 14"><polyline points="1,1 7,7 1,13" fill="none" stroke="#1b1b1b" stroke-width="0.8"/></svg><span class="service-number">04</span><span class="service-name">LIGHTING</span></li>
        <li><svg viewBox="0 0 8 14"><polyline points="1,1 7,7 1,13" fill="none" stroke="#1b1b1b" stroke-width="0.8"/></svg><span class="service-number">05</span><span class="service-name">EXTREME SPORTS</span></li>
      </ul>
      <footer class="footer-band">
        <span class="footer-address">118 Larkfield Row 07, 9th Avenue Dunmore, Calvera, 368041</span>
        <span class="footer-dot"></span>
        <span class="footer-company">VLM8 Pty Ltd</span>
        <span class="footer-nav">
          <svg viewBox="0 0 5 7"><polyline points="4,0.5 1,3.5 4,6.5" fill="none" stroke="#fff" stroke-width="1.4"/></svg>03
          <svg viewBox="0 0 5 7"><polyline points="1,0.5 4,3.5 1,6.5" fill="none" stroke="#fff" stroke-width="1.4"/></svg>
        </span>
      </footer>
    </div>
    <p class="page-caption">3rd page</p>
  </section>

  <!-- page 4 -->
  <section class="slide-frame slide-frame--4">
    <div class="slide">
      <div class="top-tab"></div>
      <div class="brand-mark"><span class="dot"></span>VLM8</div>
      <div class="section-panel"></div>
      <h2 class="section-label section-label--services">SERVICES</h2>
      <svg class="section-icon" viewBox="0 0 12 12" aria-hidden="true">
        <circle cx="6" cy="6" r="4.5" fill="none" stroke="#fff" stroke-width="1.2"/>
      </svg>
      <div class="photo-area photo-area--it" role="img" aria-label="Photo of a hand touching glowing icons in front of server racks"></div>
      <div class="accent-block accent-block--it"></div>
      <h3 class="service-heading">&gt; 01 INFORMATION<span>TECHNOLOGY</span></h3>
      <div class="body-copy body-copy--it">
        <p>The company has a vision for the fast and effective delivery of IT as a Service (ITaaS). VLM8 aim to provide their customers with the flexibility of choice to define and acquire only the specific services they require, along with when and where they need them. The company has formed a consultancy with significant knowledge and experience in the provision of service oriented IT.</p>
        <p>VLM8 aims to help their client's source and operate their IT systems in the most efficient and effective way. With competencies ranging from Strategy and Programme Management, Optimisation, VLM8 partner with their clients to realize the business value of service based IT.</p>
      </div>
      <footer class="footer-band">
        <span class="footer-address">118 Larkfield Row 07, 9th Avenue Dunmore, Calvera, 368041</span>
        <span class="footer-dot"></span>
        <span class="footer-company">VLM8 Pty Ltd</span>
        <span class="footer-nav">
          <svg viewBox="0 0 5 7"><polyline points="4,0.5 1,3.5 4,6.5" fill="none" stroke="#fff" stroke-width="1.4"/></svg>04
          <svg viewBox="0 0 5 7"><polyline points="1,0.5 4,3.5 1,6.5" fill="none" stroke="#fff" stroke-width="1.4"/></svg>
        </span>
      </footer>
    </div>
    <p class="page-caption">4th page</p>
  </section>
</body>
</html>
```